Garden Design Flier

I would like a PDF of this half page A4 flier in soft green tones with dark green leaves.

Target Market(s)

Home owners and real estate agents

Font styles to use
Serif
Other font styles liked:
• Papyrus

Colors
acd136
9bcb3c
cadf82
fefdec

Requirements
Must have
• Green tones
Nice to have
• Leaves, vines, lawns
Should not have
• Open to ideas, but classic style

```html
<!DOCTYPE html>
<html lang="en">
<head>
<meta charset="utf-8">
<title>Parterre Gardens – Flier</title>
<link rel="stylesheet" href="https://fonts.googleapis.com/css2?family=Alegreya:wght@400;500&family=Marcellus&display=swap">
<style>
  :root {
    --backdrop: #5f5f5f;
    --paper: #ffffff;
    --sage-light: #a6cf9f;
    --sage: #80b874;
    --wordmark: #72a96f;
    --ink-light: #ffffff;
    --photo-pale: #f2f8f0;
    --photo-mid: #cfe6cb;
    --photo-deep: #6fb06c;
  }
  * { box-sizing: border-box; margin: 0; padding: 0; }
  html, body {
    width: 1040px;
    height: 1200px;
    overflow: hidden;
    background: var(--backdrop);
  }
  .flier {
    position: absolute;
    left: 117px;
    top: 30px;
    width: 882px;
    height: 1248px;
    background: var(--paper);
    transform: scale(0.9135);
    transform-origin: top left;
    overflow: hidden;
  }
  .foliage-photo {
    position: absolute;
    left: 0; top: 0;
    width: 470px; height: 1248px;
    background:
      radial-gradient(ellipse 60% 35% at 30% 40%, rgba(111,176,108,0.55), transparent 70%),
      radial-gradient(ellipse 55% 40% at 55% 85%, rgba(111,176,108,0.65), transparent 70%),
      linear-gradient(180deg, var(--photo-pale) 0%, var(--photo-mid) 55%, #b4d9ae 100%);
  }
  .top-block {
    position: absolute;
    left: 469px; top: 0;
    width: 366px; height: 194px;
    background: var(--sage-light);
  }
  .wordmark {
    position: absolute;
    left: 276px; top: 205px;
    width: 564px; height: 120px;
  }
  .wordmark text {
    font-family: "Marcellus", serif;
    font-size: 132px;
    fill: var(--wordmark);
  }
  .info-panel {
    position: absolute;
    left: 469px; top: 325px;
    width: 366px; height: 923px;
    background: var(--sage);
    color: var(--ink-light);
    font-family: "Alegreya", serif;
    padding: 30px 0 0 27px;
  }
  .business-line { font-size: 21px; line-height: 32px; }
  .credential { font-size: 19px; line-height: 25px; margin-top: 22px; }
  .rule {
    width: 311px;
    height: 0;
    border-top: 1.5px solid var(--ink-light);
    margin-left: 2px;
  }
  .rule--upper { margin-top: 32px; }
  .services {
    list-style: none;
    margin: 50px 0 42px;
  }
  .services li {
    display: flex;
    align-items: center;
    height: 60.5px;
    font-family: "Marcellus", serif;
    font-size: 47px;
    letter-spacing: 0.5px;
  }
  .services svg { width: 36px; height: 40px; margin-right: 28px; flex: none; }
  .blurb { font-size: 19px; line-height: 25px; margin-top: 26px; }
  .blurb + .blurb { margin-top: 16px; }
  .contact { font-size: 19px; line-height: 29.5px; margin-top: 32px; }
</style>
</head>
<body>
  <div class="flier">
    <div class="foliage-photo" role="img" aria-label="Soft-focus photograph of fresh green leaves on slender stems against a pale misty background"></div>
    <div class="top-block"></div>

    <svg class="wordmark" viewBox="0 0 564 120" aria-label="Parterre">
      <text x="0" y="108" textLength="562" lengthAdjust="spacingAndGlyphs">PARTERRE</text>
    </svg>

    <section class="info-panel">
      <p class="business-line">GARDENS<br>by Daniel Harrow</p>
      <p class="credential">Certificate 3, Horticulture,<br>Ridgeway Institute</p>
      <div class="rule rule--upper"></div>

      <ul class="services">
        <li><svg viewBox="0 0 36 40" aria-hidden="true"><path d="M4 36 C2 18 12 4 32 3 C34 22 24 36 4 36 Z" fill="#fff"/><path d="M6 34 L28 8 M12 27 L12 17 M12 27 L22 27 M18 20 L18 12 M18 20 L27 20" stroke="#80b874" stroke-width="2.2" fill="none" stroke-linecap="round"/></svg>DESIGN</li>
        <li><svg viewBox="0 0 36 40" aria-hidden="true"><path d="M4 36 C2 18 12 4 32 3 C34 22 24 36 4 36 Z" fill="#fff"/><path d="M6 34 L28 8 M12 27 L12 17 M12 27 L22 27 M18 20 L18 12 M18 20 L27 20" stroke="#80b874" stroke-width="2.2" fill="none" stroke-linecap="round"/></svg>INSTALL</li>
        <li><svg viewBox="0 0 36 40" aria-hidden="true"><path d="M4 36 C2 18 12 4 32 3 C34 22 24 36 4 36 Z" fill="#fff"/><path d="M6 34 L28 8 M12 27 L12 17 M12 27 L22 27 M18 20 L18 12 M18 20 L27 20" stroke="#80b874" stroke-width="2.2" fill="none" stroke-linecap="round"/></svg>GROW</li>
        <li><svg viewBox="0 0 36 40" aria-hidden="true"><path d="M4 36 C2 18 12 4 32 3 C34 22 24 36 4 36 Z" fill="#fff"/><path d="M6 34 L28 8 M12 27 L12 17 M12 27 L22 27 M18 20 L18 12 M18 20 L27 20" stroke="#80b874" stroke-width="2.2" fill="none" stroke-linecap="round"/></svg>TEND</li>
        <li><svg viewBox="0 0 36 40" aria-hidden="true"><path d="M4 36 C2 18 12 4 32 3 C34 22 24 36 4 36 Z" fill="#fff"/><path d="M6 34 L28 8 M12 27 L12 17 M12 27 L22 27 M18 20 L18 12 M18 20 L27 20" stroke="#80b874" stroke-width="2.2" fill="none" stroke-linecap="round"/></svg>ENJOY</li>
      </ul>

      <div class="rule"></div>
      <p class="blurb">All your gardening and landscaping<br>needs from design and installation<br>to general maintenance</p>
      <p class="blurb">Bespoke vegetable gardens and<br>potager created to suite your site<br>and requirements</p>
      <p class="contact">E: daniel@parterregardens.com.au<br>M: 0400-318252<br>ABN: 51902736418</p>
    </section>
  </div>
</body>
</html>
```